Hybrid education and entertainment company needs help with creating dynamic school worksheets

I'm looking for a skilled individual to create a versatile Microsoft Word template for school worksheets for Lessonvibe. Your task will involve:
- Designing a user-friendly and visually appealing template that can be easily customized for various subjects and grade levels.
- Ensuring the template includes sections for titles, instructions, questions, and space for student responses.
- Incorporating consistent formatting and styles to maintain a professional look across all worksheets.
- Adding placeholders for images, graphics, or interactive elements to enhance engagement.
- Testing the template to ensure compatibility and ease of use for educators.
Your work will help streamline the worksheet creation process, making it easier for educators to develop effective and engaging learning materials.

```html
<!DOCTYPE html>
<html lang="en">
<head>
<meta charset="utf-8">
<title>Lessonvibe Worksheet Template – Pages 20-27</title>
<link href="https://fonts.googleapis.com/css2?family=Poppins:wght@400&family=Playfair+Display:wght@500&family=Cormorant+Garamond:wght@500&family=Tinos&display=swap" rel="stylesheet">
<style>
  :root{
    --backdrop:#575757;
    --paper:#fdf9f3;
    --ink:#4a4a4a;
    --ink-head:#3f3f3f;
    --ink-soft:#6b6b6b;
    --lavender:#b9b1be;
    --lavender-mid:#c6c0cb;
    --lavender-light:#d5d1d9;
    --mist:#dcd8dc;
    --sand:#e6dfd3;
    --sand-light:#ece7dc;
    --pill:#e4e1e2;
    --ornament:#d9d2cc;
    --white:#ffffff;
  }
  html,body{margin:0;padding:0;}
  body{
    width:1200px;height:3036px;overflow:hidden;position:relative;
    background:var(--backdrop);
  }
  .range-title{
    position:absolute;left:0;top:28px;width:1200px;text-align:center;
    font-family:"Poppins",sans-serif;font-weight:400;font-size:190px;line-height:190px;
    color:var(--white);letter-spacing:-2px;margin:0;
  }
  .spread{position:absolute;left:83px;width:1053px;height:681px;display:block;}
  .spread-1{top:223px}.spread-2{top:917px}.spread-3{top:1611px}.spread-4{top:2306px}
  .page-bg{fill:var(--paper)}
  .gutter{stroke:#efe9e0;stroke-width:.8}
  .head-text{font-family:"Tinos",serif;font-size:6.4px;fill:var(--ink-head)}
  .head-rule{stroke:var(--ink-soft);stroke-width:.6}
  .rule{stroke:var(--ink);stroke-width:.6;fill:none}
  .frame{fill:none;stroke:var(--ink);stroke-width:.8}
  .label{font-family:"Tinos",serif;font-size:8.4px;fill:#2f2f2f}
  .label-caps{font-family:"Tinos",serif;font-size:8px;fill:#2f2f2f;letter-spacing:.2px}
  .label-light{font-family:"Tinos",serif;font-size:8.6px;fill:var(--white);letter-spacing:.2px}
  .section-title{font-family:"Playfair Display",serif;font-weight:500;font-size:28px;fill:var(--ink-soft)}
  .page-heading{font-family:"Cormorant Garamond",serif;font-weight:500;font-size:22px;fill:#2a2a2a;letter-spacing:.6px}
  .fill-lavender{fill:var(--lavender)}
  .fill-lavender-mid{fill:var(--lavender-mid)}
  .fill-lavender-light{fill:var(--lavender-light)}
  .fill-mist{fill:var(--mist)}
  .fill-sand{fill:var(--sand)}
  .fill-sand-light{fill:var(--sand-light)}
  .fill-pill{fill:var(--pill)}
  .ornament{fill:var(--ornament)}
  .star{fill:none;stroke:var(--ink);stroke-width:.7}
</style>
</head>
<body>

<h1 class="range-title">20-27</h1>

<!-- Spread: pages 20–21 -->
<svg class="spread spread-1" viewBox="0 0 894 578" xmlns="http://www.w3.org/2000/svg">
  <rect class="page-bg" width="894" height="578"/>
  <line class="gutter" x1="447" y1="0" x2="447" y2="578"/>
  <g class="page-header">
    <text class="head-text" x="30" y="34">Lessonvibe Worksheet</text>
    <text class="head-text" x="292" y="34">20</text>
    <text class="head-text" x="326" y="34">School</text>
    <text class="head-text" x="381" y="34">Template</text>
    <text class="head-text" x="477" y="34">Lessonvibe Worksheet</text>
    <text class="head-text" x="738" y="34">21</text>
    <text class="head-text" x="773" y="34">School</text>
    <text class="head-text" x="828" y="34">Template</text>
    <line class="head-rule" x1="12" y1="42" x2="880" y2="42"/>
  </g>

  <g class="todo-page">
    <text class="section-title" transform="translate(52 321) rotate(-90)" text-anchor="middle">Section Title</text>
    <circle class="frame" cx="42" cy="455" r="11"/>
    <rect class="fill-lavender" x="77" y="89" width="164" height="22" rx="11"/>
    <text class="label-light" x="159" y="103" text-anchor="middle">THINGS TO DO!</text>
    <path class="rule" d="M79 141H241M79 165H241M79 188H241M79 212H241M79 236H241M79 260H241M79 283H241M79 307H241M79 331H241M79 354H241M79 378H241M79 402H241M79 425H241M79 449H241M79 473H241M79 497H241M79 520H241M103 122V520"/>
    <rect class="frame" x="253" y="77" width="154" height="212" rx="6"/>
    <rect class="fill-lavender-light" x="253" y="298" width="154" height="225" rx="6"/>
    <text class="label-caps" x="330" y="316" text-anchor="middle">DEADLINE</text>
  </g>

  <g class="reflection-page">
    <rect class="ornament" x="647" y="75" width="100" height="6" rx="3" role="img" aria-label="Decorative wavy line ornament"/>
    <line class="rule" x1="764" y1="87" x2="849" y2="87"/>
    <rect class="fill-lavender-mid" x="491" y="104" width="228" height="23" rx="11.5"/>
    <text class="label-light" x="605" y="118.5" text-anchor="middle">3 THINGS YOU'VE LEARNED TODAY</text>
    <rect class="frame" x="491" y="133" width="228" height="44" rx="6"/>
    <rect class="frame" x="491" y="182" width="228" height="44" rx="6"/>
    <rect class="frame" x="491" y="231" width="228" height="44" rx="6"/>
    <rect class="frame" x="727" y="104" width="123" height="171" rx="6"/>
    <text class="label-caps" x="742" y="122">WHAT WENT WELL</text>
    <text class="label-caps" x="742" y="133">TODAY?</text>
    <path class="rule" d="M738 145H838M738 164H838M738 183H838M738 203H838M738 222H838M738 242H838M738 261H838"/>
    <rect class="fill-sand" x="491" y="282" width="175" height="170" rx="5"/>
    <text class="label-caps" x="506" y="299">WHAT DIDN'T GO WELL TODAY?</text>
    <rect class="fill-sand" x="674" y="282" width="176" height="170" rx="5"/>
    <text class="label-caps" x="762" y="299" text-anchor="middle">ANY OTHER THOUGHTS</text>
    <text class="label-caps" x="762" y="310" text-anchor="middle">OR FEELINGS?</text>
    <rect class="frame" x="491" y="460" width="359" height="63" rx="6"/>
    <text class="label-caps" x="506" y="483">WHAT WILL YOU</text>
    <text class="label-caps" x="506" y="495">DO DIFFERENTLY</text>
    <text class="label-caps" x="506" y="506">TOMORROW?</text>
    <path class="rule" d="M607 486H836M607 509H836"/>
  </g>
</svg>

<!-- Spread: pages 22–23 -->
<svg class="spread spread-2" viewBox="0 0 894 578" xmlns="http://www.w3.org/2000/svg">
  <rect class="page-bg" width="894" height="578"/>
  <line class="gutter" x1="447" y1="0" x2="447" y2="578"/>
  <g class="page-header">
    <text class="head-text" x="30" y="34">Lessonvibe Worksheet</text>
    <text class="head-text" x="292" y="34">22</text>
    <text class="head-text" x="326" y="34">School</text>
    <text class="head-text" x="381" y="34">Template</text>
    <text class="head-text" x="477" y="34">Lessonvibe Worksheet</text>
    <text class="head-text" x="738" y="34">23</text>
    <text class="head-text" x="773" y="34">School</text>
    <text class="head-text" x="828" y="34">Template</text>
    <line class="head-rule" x1="12" y1="42" x2="880" y2="42"/>
  </g>

  <g class="blocks-page">
    <text class="section-title" transform="translate(52 230) rotate(-90)" text-anchor="middle">Section Title</text>
    <rect class="ornament" x="45" y="327" width="6" height="200" rx="3" role="img" aria-label="Decorative vertical wavy line ornament"/>
    <rect class="fill-sand-light" x="77" y="88" width="330" height="138" rx="6"/>
    <text class="label" x="96" y="114">Type Title Name</text>
    <path class="rule" d="M96 140H380M96 161H380M96 183H380M96 204H380"/>
    <rect class="fill-lavender-light" x="77" y="235" width="168" height="22" rx="11"/>
    <text class="label" x="100" y="249">Type Title Name</text>
    <path class="rule" d="M77 289H241M77 309H241M77 329H241M77 349H241M77 369H241M103 268V369"/>
    <rect class="fill-mist" x="77" y="383" width="164" height="143" rx="6"/>
    <text class="label" x="91" y="399">Type Title Name</text>
    <rect class="frame" x="258" y="235" width="149" height="291" rx="6"/>
    <text class="label" x="271" y="265">Type Title Name</text>
    <path class="rule" d="M271 289H393M271 309H393M271 329H393M271 349H393M271 369H393"/>
    <text class="label" x="271" y="407">Type Title Name</text>
    <path class="rule" d="M271 430H393M271 450H393M271 470H393M271 490H393M271 510H393"/>
  </g>

  <g class="notes-page">
    <text class="page-heading" x="675" y="88" text-anchor="middle">Notes</text>
    <path class="rule" d="M474 108H867M474 132H867M474 157H867M474 181H867M474 205H867M474 230H867M474 254H867M474 278H867M474 303H867M474 327H867M474 351H867M474 376H867M474 400H867M474 425H867M474 449H867M474 473H867M474 498H867M474 522H867"/>
  </g>
</svg>

<!-- Spread: pages 24–25 -->
<svg class="spread spread-3" viewBox="0 0 894 578" xmlns="http://www.w3.org/2000/svg">
  <rect class="page-bg" width="894" height="578"/>
  <line class="gutter" x1="447" y1="0" x2="447" y2="578"/>
  <g class="page-header">
    <text class="head-text" x="30" y="34">Lessonvibe Worksheet</text>
    <text class="head-text" x="292" y="34">24</text>
    <text class="head-text" x="326" y="34">School</text>
    <text class="head-text" x="381" y="34">Template</text>
    <text class="head-text" x="477" y="34">Lessonvibe Worksheet</text>
    <text class="head-text" x="738" y="34">25</text>
    <text class="head-text" x="773" y="34">School</text>
    <text class="head-text" x="828" y="34">Template</text>
    <line class="head-rule" x1="12" y1="42" x2="880" y2="42"/>
  </g>

  <g class="lined-page">
    <text class="page-heading" x="230" y="87" text-anchor="middle">A SIMPLE TITLE</text>
    <path class="rule" d="M28 108H420M28 132H420M28 157H420M28 181H420M28 205H420M28 230H420M28 254H420M28 278H420M28 303H420M28 327H420M28 351H420M28 376H420M28 400H420M28 425H420M28 449H420M28 473H420M28 498H420M28 522H420"/>
  </g>

  <g class="word-grid-page">
    <rect class="fill-pill" x="488" y="113" width="102" height="22" rx="11"/>
    <text class="label" x="539" y="127" text-anchor="middle">Title</text>
    <rect class="fill-pill" x="596" y="113" width="258" height="22" rx="11"/>
    <text class="label" x="725" y="127" text-anchor="middle">Title Here</text>
    <rect class="frame" x="488" y="142" width="366" height="377" rx="6"/>
    <path class="rule" d="M593 142V519M622 142V519M651 142V519M680 142V519M710 142V519M739 142V519M768 142V519M797 142V519M826 142V519"/>
    <path class="rule" d="M593 167H854M593 192H854M593 243H854M593 268H854M593 318H854M593 343H854M593 393H854M593 418H854M593 468H854M593 494H854"/>
    <path class="rule" d="M488 218H854M488 293H854M488 368H854M488 443H854"/>
    <text class="label" x="540" y="180" text-anchor="middle">Word 1</text>
    <text class="label" x="540" y="243" text-anchor="middle">Word 2</text>
    <text class="label" x="540" y="316" text-anchor="middle">Word 3</text>
    <text class="label" x="540" y="389" text-anchor="middle">Word 4</text>
    <text class="label" x="540" y="462" text-anchor="middle">Word 5</text>
  </g>
</svg>

<!-- Spread: pages 26–27 -->
<svg class="spread spread-4" viewBox="0 0 894 578" xmlns="http://www.w3.org/2000/svg">
  <defs>
    <path id="star-shape" class="star" d="M0 -10L2.47 -3.4L9.51 -3.09L3.99 1.3L5.88 8.09L0 4.2L-5.88 8.09L-3.99 1.3L-9.51 -3.09L-2.47 -3.4Z"/>
    <g id="rating-row">
      <rect class="frame" x="36" y="0" width="216" height="22" rx="11"/>
      <use href="#star-shape" x="277" y="11"/>
      <use href="#star-shape" x="305" y="11"/>
      <use href="#star-shape" x="332" y="11"/>
      <use href="#star-shape" x="360" y="11"/>
      <use href="#star-shape" x="387" y="11"/>
    </g>
  </defs>
  <rect class="page-bg" width="894" height="578"/>
  <line class="gutter" x1="447" y1="0" x2="447" y2="578"/>
  <g class="page-header">
    <text class="head-text" x="30" y="34">Lessonvibe Worksheet</text>
    <text class="head-text" x="292" y="34">26</text>
    <text class="head-text" x="326" y="34">School</text>
    <text class="head-text" x="381" y="34">Template</text>
    <text class="head-text" x="477" y="34">Lessonvibe Worksheet</text>
    <text class="head-text" x="738" y="34">27</text>
    <text class="head-text" x="773" y="34">School</text>
    <text class="head-text" x="828" y="34">Template</text>
    <line class="head-rule" x1="12" y1="42" x2="880" y2="42"/>
  </g>

  <g class="rating-page">
    <use href="#rating-row" y="96"/>
    <use href="#rating-row" y="125"/>
    <use href="#rating-row" y="154"/>
    <use href="#rating-row" y="183"/>
    <use href="#rating-row" y="211"/>
    <use href="#rating-row" y="240"/>
    <use href="#rating-row" y="269"/>
    <use href="#rating-row" y="300"/>
    <use href="#rating-row" y="328"/>
    <use href="#rating-row" y="357"/>
    <use href="#rating-row" y="386"/>
    <use href="#rating-row" y="415"/>
    <use href="#rating-row" y="444"/>
    <use href="#rating-row" y="473"/>
    <use href="#rating-row" y="502"/>
  </g>

  <g class="log-page">
    <text class="page-heading" x="675" y="84" text-anchor="middle">A SIMPLE TITLE</text>
    <rect class="fill-pill" x="487" y="107" width="119" height="22" rx="11"/>
    <text class="label-caps" x="500" y="121">DATE</text>
    <rect class="fill-pill" x="611" y="107" width="119" height="22" rx="11"/>
    <text class="label-caps" x="625" y="121">MONTH</text>
    <rect class="fill-pill" x="735" y="107" width="119" height="22" rx="11"/>
    <text class="label-caps" x="748" y="121">YEAR</text>
    <rect class="frame" x="487" y="136" width="365" height="58" rx="6"/>
    <text class="label" x="504" y="152">Title Here</text>
    <rect class="frame" x="487" y="203" width="365" height="320" rx="6"/>
    <path class="rule" d="M630 203V523M760 203V523M807 203V523"/>
    <path class="rule" d="M487 229H852M487 254H852M487 278H852M487 303H852M487 327H852M487 352H852M487 376H852M487 401H852M487 425H852M487 450H852M487 474H852M487 499H852"/>
    <text class="label" x="536" y="220" text-anchor="middle">Title</text>
    <text class="label" x="690" y="220" text-anchor="middle">Title</text>
    <text class="label" x="785" y="220" text-anchor="middle">Title</text>
    <text class="label" x="823" y="220" text-anchor="middle">Title</text>
  </g>
</svg>

</body>
</html>
```